Letterhead Design Project

We have just had a letterhead desinged on word which is pretty basic and boring. We are looking for a professional and modern letterhead to suit our business for letters and quotes. We are an irrigation business that looks at providing a garden enhancement package. We do instore sales, internet sales and design and installation. We would like the colours to be similar to what is on our website. www.dunsfordwatering.com.au
Industry/Entity Type
Internet
Requirements
Must have
- We would like to include:
find us on facebook and twitter,
member of sprinquest stores,
Catchphrase: "The Garden Enhancement Specialist"
Approved Watering Stockist Logo
phone, fax, email & website

```html
<!DOCTYPE html>
<html lang="en">
<head>
<meta charset="utf-8">
<title>Dunsford Watering Supplies – Letterhead</title>
<link href="https://fonts.googleapis.com/css2?family=Open+Sans:wght@400;600;700&display=swap" rel="stylesheet">
<style>
  :root {
    --backdrop: #b08a2c;
    --paper: #ffffff;
    --ink: #1a1a1a;
    --brand-blue: #3a7fc0;
    --text-grey: #3d3d3d;
    --divider: #6b6b6b;
    --ghost: #f3f5f8;
    --badge: #3f86c6;
  }
  * { box-sizing: border-box; margin: 0; padding: 0; }
  html, body { width: 1200px; height: 760px; overflow: hidden; }
  body {
    background: var(--backdrop);
    font-family: "Open Sans", Arial, sans-serif;
    position: relative;
  }
  .sheet {
    position: absolute;
    top: 42px;
    width: 517px;
    height: 668px;
    background: var(--paper);
  }
  .sheet--header-address { left: 55px; }
  .sheet--header-contacts { left: 626px; }

  .ghost-mark { position: absolute; left: 150px; top: 210px; }

  .brand {
    position: absolute;
    width: 232px;
    display: flex;
    align-items: center;
    gap: 6px;
  }
  .brand__dot {
    width: 13px; height: 13px; border-radius: 50%;
    background: var(--brand-blue);
    flex: none;
  }
  .brand__name {
    font-size: 16px;
    font-weight: 600;
    color: var(--ink);
    letter-spacing: -0.2px;
    line-height: 1;
    white-space: nowrap;
  }
  .sheet--header-address .brand { left: 66px; top: 42px; }
  .sheet--header-contacts .brand { left: 90px; top: 32px; }

  .v-rule {
    position: absolute;
    width: 1px;
    background: var(--divider);
  }

  .tagline-block {
    position: absolute;
    left: 319px; top: 38px;
    font-size: 7.5px;
    line-height: 13px;
  }
  .tag-strong { color: var(--brand-blue); font-weight: 700; }
  .tag-address { color: var(--text-grey); }

  .contact-list {
    position: absolute;
    list-style: none;
    font-size: 7.5px;
    line-height: 10.2px;
    color: var(--text-grey);
  }
  .contact-list li { display: flex; align-items: center; gap: 6px; white-space: nowrap; }
  .contact-icon { width: 7px; height: 7px; flex: none; }

  .badge {
    position: absolute;
    width: 52px; height: 52px;
    border-radius: 50%;
    background: var(--badge);
    border: 3px solid #ffffff;
    box-shadow: 0 0 0 1px var(--badge);
  }

  .footer-line {
    position: absolute;
    top: 651px;
    font-size: 7.5px;
    white-space: nowrap;
  }
</style>
</head>
<body>

<!-- Version A: address in header, contacts in footer -->
<section class="sheet sheet--header-address">
  <svg class="ghost-mark" width="240" height="230" viewBox="0 0 240 230" aria-hidden="true">
    <circle cx="120" cy="115" r="100" fill="var(--ghost)"/>
  </svg>

  <div class="brand">
    <span class="brand__dot"></span>
    <span class="brand__name">Dunsford Watering Supplies</span>
  </div>

  <div class="v-rule" style="left:308px; top:36px; height:38px;"></div>

  <div class="tagline-block">
    <p class="tag-strong">member of sprinquest stores</p>
    <p class="tag-strong">THE GARDEN ENHANCEMENT SPECIALIST</p>
    <p class="tag-address">418 Kerrigan Rd Dunsford Vic 3187</p>
  </div>

  <div class="badge" style="left:174px; top:604px;" role="img" aria-label="Approved Watering Stockist badge"></div>
  <div class="v-rule" style="left:236px; top:612px; height:38px;"></div>

  <ul class="contact-list" style="left:247px; top:606px;">
    <li><svg class="contact-icon" viewBox="0 0 8 8"><path d="M1 3a3 3 0 0 1 6 0" stroke="var(--brand-blue)" stroke-width="1.4" fill="none"/></svg>123-456-7890</li>
    <li><svg class="contact-icon" viewBox="0 0 8 8"><rect x="1" y="3" width="6" height="4" fill="var(--brand-blue)"/><rect x="2" y="1" width="4" height="2" fill="var(--brand-blue)"/></svg>123-456-7890</li>
    <li><svg class="contact-icon" viewBox="0 0 8 8"><circle cx="4" cy="4" r="3.5" fill="var(--brand-blue)"/></svg>Find us on</li>
    <li><svg class="contact-icon" viewBox="0 0 8 8"><circle cx="4" cy="4" r="3.5" fill="var(--brand-blue)"/></svg>Find us on</li>
    <li><svg class="contact-icon" viewBox="0 0 8 8"><circle cx="4" cy="4" r="3.2" fill="none" stroke="var(--brand-blue)" stroke-width="1.2"/></svg>www.dunsfordwatering.com.au</li>
  </ul>
</section>

<!-- Version B: contacts in header, address line in footer -->
<section class="sheet sheet--header-contacts">
  <svg class="ghost-mark" width="240" height="230" viewBox="0 0 240 230" aria-hidden="true">
    <circle cx="120" cy="115" r="100" fill="var(--ghost)"/>
  </svg>

  <div class="brand">
    <span class="brand__dot"></span>
    <span class="brand__name">Dunsford Watering Supplies</span>
  </div>

  <div class="v-rule" style="left:332px; top:26px; height:40px;"></div>

  <ul class="contact-list" style="left:346px; top:23px;">
    <li><svg class="contact-icon" viewBox="0 0 8 8"><path d="M1 3a3 3 0 0 1 6 0" stroke="var(--brand-blue)" stroke-width="1.4" fill="none"/></svg>123-456-7890</li>
    <li><svg class="contact-icon" viewBox="0 0 8 8"><rect x="1" y="3" width="6" height="4" fill="var(--brand-blue)"/><rect x="2" y="1" width="4" height="2" fill="var(--brand-blue)"/></svg>123-456-7890</li>
    <li><svg class="contact-icon" viewBox="0 0 8 8"><circle cx="4" cy="4" r="3.5" fill="var(--brand-blue)"/></svg>Find us on</li>
    <li><svg class="contact-icon" viewBox="0 0 8 8"><circle cx="4" cy="4" r="3.5" fill="var(--brand-blue)"/></svg>Find us on</li>
    <li><svg class="contact-icon" viewBox="0 0 8 8"><circle cx="4" cy="4" r="3.2" fill="none" stroke="var(--brand-blue)" stroke-width="1.2"/></svg>www.dunsfordwatering.com.au</li>
  </ul>

  <div class="badge" style="left:230px; top:595px;" role="img" aria-label="Approved Watering Stockist badge"></div>

  <p class="footer-line tag-address" style="left:67px;">418 Kerrigan Rd Dunsford Vic 3187</p>
  <p class="footer-line tag-strong" style="left:205px;">member of sprinquest stores</p>
  <p class="footer-line tag-strong" style="left:322px;">THE GARDEN ENHANCEMENT SPECIALIST</p>
</section>

</body>
</html>
```